Redesign of an existing homepage

This site needs a redesign
https://www.ferien-am-haldbach.de
This page with the accommodation options is important for the customer
https://www.ferien-am-haldbach.de/gastgeber/
Till now there is a new logo. See attachment. That's all I have.
It would make sense to use the colors of the logo in the redesign.
footer.jpg.
I would put this info into the footer. The graphic (Infomaterial) is not needed.
a new menu - links.jpg
This info can be put in a new menu. Therefore the right column is gone and there is more space for the design.
NEW:
Please keep in mind that the Icons are important and shall be displayed under every accommodation
Number of Pages Required
1 page

```html
<!DOCTYPE html>
<html lang="de">
<head>
<meta charset="utf-8">
<title>Tourismusverband Haldbach – Urlaub im Haldtal</title>
<link href="https://fonts.googleapis.com/css2?family=Poppins:ital,wght@0,400;0,500;0,600;0,700;1,400&display=swap" rel="stylesheet">
<style>
:root{
  --green:#7ab51d;
  --sky:#2aa1db;
  --blue:#1a70b8;
  --title:#1b7fc4;
  --footer:#1b75bb;
  --text:#555;
  --line:#cfe3a8;
  --white:#fff;
}
*{box-sizing:border-box;margin:0;padding:0}
html,body{width:1200px;height:3264px;overflow:hidden}
body{font-family:"Poppins",sans-serif;color:var(--text);background:var(--white);position:relative}
.abs{position:absolute}

/* header */
.topbar{left:225px;top:0;width:975px;height:38px;background:var(--sky);clip-path:polygon(0 0,100% 0,100% 100%,14px 100%)}
.topbar-contact{right:62px;top:4px;display:flex;gap:32px;align-items:center;color:var(--white);font-size:13.5px}
.topbar-contact span{display:flex;align-items:center;gap:12px}
.dot{width:30px;height:30px;border-radius:50%;background:var(--green);display:flex;align-items:center;justify-content:center}
.brand{left:55px;top:6px;width:140px;display:flex;flex-direction:column;align-items:center;gap:5px}
.brand-mark{width:46px;height:46px;border-radius:50%;background:var(--green)}
.brand-name{font-weight:600;font-size:11.5px;line-height:1.25;color:var(--blue);text-align:center}
.nav{right:62px;top:58px;display:flex;gap:33px;font-size:14.5px;color:var(--blue)}
.nav a{color:inherit;text-decoration:none}
.nav a.active{color:var(--green)}

/* hero */
.hero{left:0;top:98px;width:1200px;height:576px;background:linear-gradient(100deg,#5d6a4c 0%,#6f7866 30%,#4d5247 55%,#2f3330 80%,#3b3f3a 100%)}
.hero-copy{left:646px;top:258px;width:500px}
.hero-title{font-size:42px;line-height:1.07;font-weight:400;color:var(--sky)}
.hero-title b{color:var(--green);font-weight:700}
.hero-lead{margin-top:22px;font-size:13.5px;line-height:1.5;color:var(--white)}
.btn{display:inline-flex;align-items:center;justify-content:center;color:var(--white);font-weight:600;border-radius:20px;text-decoration:none}
.hero-copy .btn{margin-top:30px;width:164px;height:37px;background:var(--blue);font-size:14.5px}

/* partners */
.partners{left:219px;top:749px;display:flex;gap:22px}
.partner{width:174px;height:124px;border:1px solid var(--line);border-radius:10px;display:flex;align-items:center;justify-content:center}
.partner i{display:block;width:80px;height:80px;border-radius:50%;background:#e6eef4}

/* section heading */
.section-title{left:0;width:1200px;text-align:center;font-size:32px;font-weight:600;color:var(--sky)}

/* host cards */
.host{width:524px;height:500px;border-radius:12px;background:var(--white);box-shadow:0 2px 12px rgba(0,0,0,.08);overflow:hidden;text-align:center}
.host-photo{height:224px}
.host-name{margin-top:13px;font-size:19px;font-weight:600;color:var(--title)}
.host-addr{font-size:11.5px;color:var(--sky);margin-top:1px}
.host-desc{margin:12px auto 0;width:450px;height:78px;font-size:13px;line-height:1.5;color:var(--text)}
.amenities{margin-top:12px;display:flex;justify-content:center;gap:4px}
.amenities span{width:19px;height:19px;border:1.5px solid #333;border-radius:3px;font-size:10px;font-weight:700;line-height:16px;color:#222;display:flex;align-items:center;justify-content:center}
.price{margin-top:10px;font-size:13.5px;font-style:italic;color:var(--green)}
.host .btn{margin-top:11px;width:412px;height:37px;background:var(--blue);font-size:14.5px}

.view-more{left:517px;top:2098px;width:165px;height:36px;background:var(--green);font-size:14.5px;border-radius:18px}

/* brochures */
.brochures{left:203px;top:2278px;display:flex;gap:17px}
.brochure{width:186px;height:235px}
.arrow{width:42px;height:42px;border-radius:50%;display:flex;align-items:center;justify-content:center}
.arrow.prev{left:108px;top:2375px;background:var(--sky)}
.arrow.next{left:1050px;top:2375px;border:1.5px solid var(--sky)}

/* events */
.event{left:264px;top:2659px;width:671px;height:221px;border:1.5px solid var(--line);border-radius:14px}
.event-photo{left:16px;top:17px;width:308px;height:185px;border-radius:10px;background:linear-gradient(160deg,#c9b98f,#8a8f62 50%,#6f7b4c)}
.event-title{left:354px;top:56px;font-size:18.5px;line-height:1.3;font-weight:600;color:var(--title)}
.event .btn{left:354px;top:124px;width:165px;height:36px;background:var(--green);font-size:14.5px;position:absolute}

/* footer */
.footer{left:0;top:2939px;width:1200px;height:325px;background:var(--footer);color:var(--white)}
.f-brand{left:114px;top:55px;width:240px;text-align:center}
.f-brand .brand-mark{width:70px;height:70px;margin:0 auto 10px}
.f-brand .name{font-size:16px;font-weight:600;line-height:1.2}
.f-brand .addr{margin-top:20px;font-size:13.5px;line-height:1.7}
.f-rule{top:57px;width:1px;height:171px;background:rgba(255,255,255,.35)}
.f-head{font-size:17px;font-weight:600;color:var(--green)}
.f-contact{left:433px;top:56px}
.f-contact ul{list-style:none;margin-top:18px}
.f-contact li{display:flex;align-items:center;gap:18px;font-size:13.5px;height:34px;margin-bottom:12px}
.f-icon{width:34px;height:34px;border:1.5px solid var(--white);border-radius:50%;display:flex;align-items:center;justify-content:center}
.f-hours{left:799px;top:56px}
.f-hours table{margin-top:10px;font-size:13px;border-collapse:collapse}
.f-hours td{padding:2px 14px 2px 0}
.f-bottom{left:60px;top:275px;width:1080px;border-top:1px solid rgba(255,255,255,.3);text-align:center;padding-top:14px;font-size:12.5px}
</style>
</head>
<body>

<header>
  <div class="abs topbar"></div>
  <div class="abs topbar-contact">
    <span><i class="dot"><svg width="15" height="15" viewBox="0 0 24 24"><path fill="#fff" d="M6.6 10.8a15 15 0 0 0 6.6 6.6l2.2-2.2c.3-.3.7-.4 1-.2 1.1.4 2.3.6 3.6.6.6 0 1 .4 1 1V20c0 .6-.4 1-1 1A17 17 0 0 1 3 4c0-.6.4-1 1-1h3.5c.6 0 1 .4 1 1 0 1.3.2 2.5.6 3.6.1.3 0 .7-.2 1z"/></svg></i>+ 0123 456 789</span>
    <span><i class="dot"><svg width="15" height="15" viewBox="0 0 24 24"><path fill="#fff" d="M3 5h18v14H3z"/><path d="M3 6l9 7 9-7" stroke="#7ab51d" stroke-width="2" fill="none"/></svg></i>info@haldbach-ferien.de</span>
  </div>
  <div class="abs brand">
    <i class="brand-mark"></i>
    <div class="brand-name">TOURISMUSVERBAND<br>HALDBACH</div>
  </div>
  <nav class="abs nav">
    <a class="active" href="#">Home</a><a href="#">Gastgeber</a><a href="#">Haldtal</a><a href="#">Freizeit</a><a href="#">Ausflugsziele</a><a href="#">Kunst &amp; Kultur</a><a href="#">kontakt</a>
  </nav>
</header>

<section>
  <div class="abs hero" role="img" aria-label="Familie mit zwei Kindern vor einem Wohnhaus mit Garten"></div>
  <div class="abs hero-copy">
    <h1 class="hero-title"><b>Urlaub im Haldtal –<br>dem</b> schönsten Fleck Bayerns</h1>
    <p class="hero-lead">Kultur und Natur, Lebensfreude und Genuss, freundliche und aufgeschlossene Menschen…</p>
    <a class="btn" href="#">Contact Us</a>
  </div>
</section>

<section class="abs partners" aria-label="Partner">
  <div class="partner"><i></i></div>
  <div class="partner"><i></i></div>
  <div class="partner"><i></i></div>
  <div class="partner"><i></i></div>
</section>

<h2 class="abs section-title" style="top:942px">Gastgeber im Haldtal</h2>

<article class="abs host" style="left:60px;top:1021px">
  <div class="host-photo" role="img" aria-label="Weißes Ferienhaus mit Garten und Blumen" style="background:linear-gradient(180deg,#b9b4a8,#6f8a4e 60%,#3f5a2c)"></div>
  <h3 class="host-name">Ferienhaus Sonnenwiese F</h3>
  <p class="host-addr">Lindenweg 23, 84390 Wiesfeld</p>
  <p class="host-desc">Ein exklusives Ferienhaus für Sie alleine, vom Ferienverband mit 5 Sternen ausgezeichnet, für Menschen, welche die Ruhe suchen aber auf den Komfort nicht verzichten wollen, mit offenem Kamin, W-Lan und großem eingezäunten Garten.</p>
  <div class="amenities"><span>i</span><span>▭</span><span>▤</span><span>⌂</span><span>≈</span><span>⌐</span><span>R</span><span>▥</span><span>○</span><span>▯</span><span>∼</span><span>↑</span><span>↗</span><span>▦</span><span>◌</span><span>P</span><span>P</span><span>⌂</span><span>W</span><span>◎</span></div>
  <p class="price">ab € 90,00 für 2 Personen</p>
  <a class="btn" href="#">Zur Homepage von Ferienhaus Sonnenwiese</a>
</article>

<article class="abs host" style="left:615px;top:1021px">
  <div class="host-photo" role="img" aria-label="Großer Bauernhof mit Holzbalkonen und Wiese" style="background:linear-gradient(180deg,#a9c3cf,#d8d2c2 40%,#7a9a55 75%,#55733a)"></div>
  <h3 class="host-name">Ferienhof Brandl F</h3>
  <p class="host-addr">Seeblick 10a, 84391 Moosried</p>
  <p class="host-desc">Entspannen, relaxen und Kräfte tanken. Dies können Sie auf unserem Ferienhof mit mediterranem Flair. Beheizter Pool, große Liegewiesen mit Wintergarten, Grillplatz, Kinderspielplatz und Streicheltiere. Internet über WLAN.</p>
  <div class="amenities"><span>i</span><span>▭</span><span>▤</span><span>⌂</span><span>≈</span><span>⌐</span><span>R</span><span>▥</span><span>○</span><span>▯</span><span>∼</span><span>↑</span><span>↗</span><span>▦</span><span>◌</span><span>P</span><span>P</span><span>⌂</span><span>W</span><span>◎</span></div>
  <p class="price">ab € 50,00 für 2 Personen</p>
  <a class="btn" href="#">Zur Homepage von Ferienhof Brandl</a>
</article>

<article class="abs host" style="left:60px;top:1557px">
  <div class="host-photo" role="img" aria-label="Landhaus mit Holzbalkon und gelbem Auto davor" style="background:linear-gradient(180deg,#8aa86a,#d9d6cc 45%,#7f9a55 80%,#5a7a3a)"></div>
  <h3 class="host-name">Landhaus Moosbauer</h3>
  <p class="host-addr">Quellenstraße 1, 84392 Auhofen/Kirchdorf</p>
  <p class="host-desc">Ferienhaus am "Haldtaler Bäder- und Golfland" gelegen. Genießen Sie einen Aufenthalt in einem der Kurbäder in der Nähe, frönen Sie Ihrem Hobby "Golf" und erleben Sie das große Angebot an Golfplätzen hier im Haldtal.</p>
  <div class="amenities"><span>i</span><span>▭</span><span>▤</span><span>⌂</span><span>≈</span><span>⌐</span><span>R</span><span>▥</span><span>○</span><span>▯</span><span>∼</span><span>↑</span><span>↗</span><span>▦</span><span>◌</span><span>P</span><span>P</span><span>⌂</span><span>W</span><span>◎</span></div>
  <p class="price">ab € 38,00 für 2 Personen</p>
  <a class="btn" href="#">Zur Homepage von Landhaus Moosbauer</a>
</article>

<article class="abs host" style="left:615px;top:1557px">
  <div class="host-photo" role="img" aria-label="Alpenhof mit Blumenbalkonen vor Bergen" style="background:linear-gradient(180deg,#9fb3c2,#6d7f6a 35%,#d9d4c7 65%,#5f6f48)"></div>
  <h3 class="host-name">Ferienhof Lindner F</h3>
  <p class="host-addr">Oberseeblick 5a, 84390 Haldbach</p>
  <p class="host-desc">Unser Baby- und Kinderbauernhof, nur 3km von der schönen Stadt Haldbach entfernt, liegt inmitten einer herrlichen Hügellandschaft. Der nahe Wald sowie der romantische Bach hinterm Hof lassen Natur pur erleben,.</p>
  <div class="amenities"><span>i</span><span>▭</span><span>▤</span><span>⌂</span><span>≈</span><span>⌐</span><span>R</span><span>▥</span><span>○</span><span>▯</span><span>∼</span><span>↑</span><span>↗</span><span>▦</span><span>◌</span><span>P</span><span>P</span><span>⌂</span><span>W</span><span>◎</span></div>
  <p class="price">ab € 45,00 für 2 Personen</p>
  <a class="btn" href="#">Zur Homepage von Ferienhof Lindner</a>
</article>

<a class="abs btn view-more" href="#">View More</a>

<h2 class="abs section-title" style="top:2203px">Informationen &amp; Prospekte</h2>
<a class="abs arrow prev" href="#" aria-label="Zurück"><svg width="14" height="14" viewBox="0 0 24 24"><path d="M15 4l-8 8 8 8" stroke="#fff" stroke-width="3" fill="none"/></svg></a>
<div class="abs brochures">
  <div class="brochure" role="img" aria-label="Prospekt Gastgeberverzeichnis mit Landschaft und Wanderin" style="background:linear-gradient(180deg,#cfdbe6 0%,#8fb26a 45%,#5e9a2e 75%,#6fae2d 100%)"></div>
  <div class="brochure" role="img" aria-label="Prospekt Haldtaler Hoftour mit altem Gutshof" style="background:linear-gradient(180deg,#8db5d6 0%,#a58b78 40%,#8a5a45 75%,#6b4a38 100%)"></div>
  <div class="brochure" role="img" aria-label="Prospekt Haldbach Sehenswertes mit Pferdestatue" style="background:linear-gradient(180deg,#b6cde0 0%,#d2c8b8 40%,#4a4038 65%,#6fae2d 82%,#6fae2d 100%)"></div>
  <div class="brochure" role="img" aria-label="Prospekt Freizeitmagazin mit Blumenwiese und Bank" style="background:linear-gradient(180deg,#a7c4e0 0%,#c9d9ea 35%,#8ea96b 65%,#4f7b2f 100%)"></div>
</div>
<a class="abs arrow next" href="#" aria-label="Weiter"><svg width="14" height="14" viewBox="0 0 24 24"><path d="M9 4l8 8-8 8" stroke="#2aa1db" stroke-width="3" fill="none"/></svg></a>

<h2 class="abs section-title" style="top:2583px">Veranstaltungen</h2>
<div class="abs event">
  <div class="abs event-photo" role="img" aria-label="Gruppe von Wanderern auf einem Waldweg"></div>
  <h3 class="abs event-title">Veranstaltungen, Hinweise<br>und Neuigkeiten</h3>
  <a class="btn" href="#">Read More</a>
</div>

<footer class="abs footer">
  <div class="abs f-brand">
    <i class="brand-mark" style="display:block;background:var(--white)"></i>
    <div class="name">TOURISMUSVERBAND<br>HALDBACH</div>
    <p class="addr">Marktplatz 1<br>84390 Haldbach</p>
  </div>
  <div class="abs f-rule" style="left:410px"></div>
  <div class="abs f-contact">
    <h4 class="f-head">Contact Us</h4>
    <ul>
      <li><i class="f-icon"><svg width="14" height="14" viewBox="0 0 24 24"><path fill="#fff" d="M6.6 10.8a15 15 0 0 0 6.6 6.6l2.2-2.2c.3-.3.7-.4 1-.2 1.1.4 2.3.6 3.6.6.6 0 1 .4 1 1V20c0 .6-.4 1-1 1A17 17 0 0 1 3 4c0-.6.4-1 1-1h3.5c.6 0 1 .4 1 1 0 1.3.2 2.5.6 3.6.1.3 0 .7-.2 1z"/></svg></i>+ 08570 / 412 3140</li>
      <li><i class="f-icon"><svg width="14" height="14" viewBox="0 0 24 24"><rect x="3" y="8" width="18" height="12" rx="2" fill="#fff"/><rect x="7" y="3" width="10" height="6" fill="none" stroke="#fff" stroke-width="2"/></svg></i>+ 08570 / 412 3149</li>
      <li><i class="f-icon"><svg width="14" height="14" viewBox="0 0 24 24"><path fill="#fff" d="M3 5h18v14H3z"/><path d="M3 6l9 7 9-7" stroke="#1b75bb" stroke-width="2" fill="none"/></svg></i>info@haldbach-ferien.de</li>
    </ul>
  </div>
  <div class="abs f-rule" style="left:777px"></div>
  <div class="abs f-hours">
    <h4 class="f-head">Opening hours</h4>
    <table>
      <tr><td>Mon–Thurs</td><td>9:00 – 16:00</td></tr>
      <tr><td>Fri</td><td>9:00 – 12:30</td></tr>
    </table>
  </div>
  <p class="abs f-bottom">© Tourismusverbandhaldbach. All rights reserved</p>
</footer>

</body>
</html>
```